Wedding expo flyer design

My name is Dorian Whitcombe and my business is called vowsbyharlow and I am a celebrant who is based in Perth Western Australia.
I am exhibiting at an expo at Gilded Arena in September and this is a DL flyer with entry details for a competition. I want my details on it for the customer to keep and the other half is the entry return with their contact details.
By filling in your details and placing this entry form in the competition box at Dorian's booth you could win.
The first prize is a $700.00 travel voucher from Vowsbyharlow and Skylark Voyages Denholm, second Prize is 2a free wedding to the value of $600.00 and third prize is 2 bottles of Varenne et Baudry Champagne.
I would like to see a modern bridal design with colours hot pink, gold and white.

Target Market(s)

22-35 year olds

Industry/Entity Type

Wedding

Logo Text

Vowsbyharlow ebridal competition

Logo styles of interest
Pictorial/Combination Logo
Requirements
Must have
• Dorian Whitcombe is a vibrant and competent local Perth celebrant (B47286) who has performed over 70 individualized weddings, commitment ceremonies, renewal of vows, funerals and naming ceremonies in and around Perth and the South West of WA and even as far away as the Isle of Pines in the South Pacific.
By booking Dorian now you will ensure a 10% discount and have a ceremony to remember.
Contact Dorian on m. 0491625803 e. dorian@vowsbyharlow.example w.www.vowsbyharlow.example p. PO Box 318 Larkfield Rise 6082 WA.

```html
<!DOCTYPE html>
<html lang="en">
<head>
<meta charset="utf-8">
<title>Dorian Whitcombe – Celebrant Competition Flyer</title>
<link href="https://fonts.googleapis.com/css2?family=Caladea:ital,wght@0,400;0,700;1,400&family=Carlito:wght@400;700&display=swap" rel="stylesheet">
<style>
  :root {
    --ink: #1d1b1b;
    --red: #e0221f;
    --contact-bg: #fdf1c4;
    --gold-bar: #f3edb9;
    --pink-bar: #fbdfe3;
    --lilac-bar: #f6e0ee;
    --swatch-gold: #c9892c;
    --swatch-red: #d9201e;
    --swatch-magenta: #c41c8c;
    --dots: #333;
    --paper: #ffffff;
  }
  * { margin: 0; padding: 0; box-sizing: border-box; }
  html, body { width: 1200px; height: 2607px; overflow: hidden; background: var(--paper); }
  .flyer {
    position: relative; width: 1200px; height: 2607px; overflow: hidden;
    background: var(--paper); color: var(--ink);
    font-family: "Caladea", Georgia, serif;
  }
  .cake-photo { position: absolute; top: 0; left: 860px; width: 340px; height: 1560px; }
  .ribbons { position: absolute; top: 0; left: 0; width: 1200px; height: 2607px; pointer-events: none; }

  .intro {
    position: absolute; left: 70px; top: 44px;
    font-size: 44px; line-height: 55px; white-space: nowrap;
  }
  .intro .drop { font-size: 68px; }
  .offer {
    position: absolute; left: 66px; top: 522px;
    font-size: 45px; line-height: 55px; font-style: italic; white-space: nowrap;
  }
  .contact {
    position: absolute; left: 42px; top: 705px; width: 736px; height: 378px;
    border-radius: 24px; font-style: normal;
    background: linear-gradient(90deg, var(--contact-bg) 72%, rgba(253,241,196,0.35) 100%);
    padding: 6px 0 0 24px;
    font-size: 42px; line-height: 63.5px; white-space: nowrap;
  }
  .contact .heading { color: var(--red); }

  .entry-call {
    position: absolute; left: 0; top: 1112px; width: 1140px;
    text-align: center; color: var(--red); white-space: nowrap;
  }
  .entry-call .l1 { font-size: 40px; line-height: 80px; }
  .entry-call .l2 { font-size: 46px; line-height: 80px; }
  .entry-call .l3 { font-size: 58px; line-height: 82px; font-weight: 700; }
  .entry-call .big { font-size: 56px; font-weight: 700; }
  .entry-call .small { font-size: 36px; }
  .entry-call .win { font-size: 80px; font-weight: 700; }
  .entry-call .soft { font-weight: 400; font-size: 48px; }

  .prize {
    position: absolute; left: 0; width: 1053px; display: flex; align-items: center;
    font-size: 41px; line-height: 52px; white-space: nowrap;
  }
  .prize .swatch { width: 93px; align-self: stretch; flex: none; }
  .prize .text { padding-left: 12px; }
  .prize-first { top: 1401px; height: 112px; background: var(--gold-bar); }
  .prize-first .swatch { background: linear-gradient(135deg, #a8621c, var(--swatch-gold) 50%, #e9b765); }
  .prize-second { top: 1538px; height: 110px; background: linear-gradient(90deg, var(--pink-bar) 75%, rgba(251,223,227,0.2)); }
  .prize-second .swatch { background: linear-gradient(135deg, #a80f10, var(--swatch-red) 55%, #f0552d); }
  .prize-third { top: 1673px; height: 122px; background: linear-gradient(90deg, var(--lilac-bar) 75%, rgba(246,224,238,0.2)); }
  .prize-third .swatch { background: linear-gradient(135deg, #8d0f6a, var(--swatch-magenta) 55%, #e46bc0); }
  .prize .amount { font-weight: 700; font-size: 44px; }
  .prize .wide { font-size: 46px; }

  .entry-form {
    position: absolute; left: 52px; top: 1880px; width: 1090px;
    font-family: "Carlito", Arial, sans-serif;
  }
  .entry-form .instruction { font-size: 31px; line-height: 46px; margin-bottom: 46px; white-space: nowrap; }
  .field { display: flex; align-items: baseline; font-size: 40px; height: 84px; line-height: 84px; width: 1070px; }
  .field .fill { flex: 1; height: 4px; border-bottom: 4px dotted var(--dots); margin-left: 4px; }
  .field.short { width: 890px; }
  .field.short .fill { margin-left: 0; }
  .entry-form .thanks { text-align: center; font-size: 33px; margin-top: 40px; width: 1006px; }
</style>
</head>
<body>
<main class="flyer">

  <svg class="cake-photo" viewBox="0 0 340 1560" role="img" aria-label="Photograph of a tall tiered white and gold wedding cake with a red curtain edge">
    <defs>
      <linearGradient id="cakeTone" x1="0" y1="0" x2="0" y2="1">
        <stop offset="0" stop-color="#6e4236"/>
        <stop offset="0.1" stop-color="#e2cdb0"/>
        <stop offset="0.25" stop-color="#f3e8d8"/>
        <stop offset="0.38" stop-color="#d8bd8f"/>
        <stop offset="0.5" stop-color="#f0e6dc"/>
        <stop offset="0.62" stop-color="#ffffff"/>
      </linearGradient>
      <linearGradient id="curtain" x1="0" y1="0" x2="1" y2="0">
        <stop offset="0" stop-color="#f7b0b4"/>
        <stop offset="0.5" stop-color="#e2232f"/>
        <stop offset="1" stop-color="#b8121d"/>
      </linearGradient>
      <linearGradient id="fadeDown" x1="0" y1="0" x2="0" y2="1">
        <stop offset="0" stop-color="#fff"/>
        <stop offset="0.38" stop-color="#fff"/>
        <stop offset="0.62" stop-color="#000"/>
      </linearGradient>
      <mask id="fadeMask"><rect width="340" height="1560" fill="url(#fadeDown)"/></mask>
    </defs>
    <g mask="url(#fadeMask)">
      <path d="M24 0 H340 V1560 H150 C110 1200 70 800 60 500 C55 300 40 120 24 0 Z" fill="url(#cakeTone)"/>
      <path d="M0 0 H38 C50 180 58 400 74 650 C88 860 120 1100 160 1560 H132 C96 1200 60 900 42 650 C26 420 14 180 0 0 Z" fill="url(#curtain)"/>
    </g>
  </svg>

  <svg class="ribbons" viewBox="0 0 1200 2607" aria-hidden="true">
    <defs>
      <linearGradient id="violet" x1="0" y1="0" x2="0" y2="1">
        <stop offset="0" stop-color="#e9a9e4" stop-opacity="0"/>
        <stop offset="0.25" stop-color="#dd8ee0" stop-opacity="0.7"/>
        <stop offset="1" stop-color="#eec0ec" stop-opacity="0.55"/>
      </linearGradient>
      <linearGradient id="amber" x1="0" y1="0" x2="0" y2="1">
        <stop offset="0" stop-color="#f7d37a" stop-opacity="0"/>
        <stop offset="0.5" stop-color="#f6c54b" stop-opacity="0.85"/>
        <stop offset="1" stop-color="#f4a93a" stop-opacity="0.9"/>
      </linearGradient>
    </defs>
    <path d="M1200 950 C1120 1300 1080 1700 1030 2100 C1010 2300 990 2480 980 2607 H1060 C1080 2400 1110 2100 1150 1800 C1180 1560 1200 1400 1200 1300 Z" fill="url(#violet)"/>
    <path d="M1200 1050 C1150 1400 1120 1800 1080 2200 C1065 2380 1050 2500 1040 2607 H1120 C1130 2420 1150 2200 1180 1900 C1195 1760 1200 1600 1200 1500 Z" fill="url(#violet)"/>
    <path d="M1200 1900 C1140 2100 1080 2350 1020 2607 H1110 C1140 2400 1175 2200 1200 2060 Z" fill="url(#amber)"/>
    <path d="M1200 2150 C1160 2300 1130 2460 1110 2607 H1170 C1180 2480 1190 2360 1200 2280 Z" fill="#f8e38a" fill-opacity="0.8"/>
  </svg>

  <p class="intro">
    <span class="drop">D</span><strong>orian Whitcombe</strong> is a vibrant and<br>
    competent local Perth celebrant (B47286)<br>
    who has performed over 70 individualized<br>
    weddings, commitment ceremonies, re-<br>
    newal of vows, funerals and naming cer-<br>
    emonies in and around Perth and the South<br>
    West of WA and even as far away as the<br>
    Isle of Pines in the South Pacific.
  </p>

  <p class="offer">
    By booking Dorian now you will ensure<br>
    a 10% discount and have a ceremony to<br>
    &nbsp;remember.
  </p>

  <address class="contact">
    <div class="heading">Contact Dorian on</div>
    <div>m. 0491625803</div>
    <div>e.&nbsp; dorian@vowsbyharlow.example</div>
    <div>w. www.vowsbyharlow.example</div>
    <div>p.&nbsp; PO Box 318 Larkfield Rise 6082<br>WA.</div>
  </address>

  <section class="entry-call">
    <p class="l1">By filling in <span class="big">your details</span> and placing this</p>
    <p class="l2">entry form <span class="small">in the</span> competition box at</p>
    <p class="l3">Dorian's booth <span class="soft">you could</span> <span class="win">win.</span></p>
  </section>

  <div class="prize prize-first">
    <span class="swatch"></span>
    <p class="text">The First prize is a <span class="amount">$700.00</span> travel voucher from<br><strong class="amount">Vowsbyharlow</strong> and <strong class="amount">Skylark Voyages Denholm</strong></p>
  </div>
  <div class="prize prize-second">
    <span class="swatch"></span>
    <p class="text">Second Prize is 2a <span class="wide">Free Wedding</span> to the<br>value of <span class="amount">$600.00</span></p>
  </div>
  <div class="prize prize-third">
    <span class="swatch"></span>
    <p class="text">&nbsp;Third prize is 2 bottles of <strong class="amount">Varenne et Baudry</strong><br><strong class="amount">Champagne.</strong></p>
  </div>

  <form class="entry-form">
    <p class="instruction">Please fill below details and drop it to Competition Box at Dorian’s booth</p>
    <div class="field"><span>Name:</span><span class="fill"></span></div>
    <div class="field"><span>Date of birth:</span><span class="fill"></span></div>
    <div class="field"><span>Address:</span><span class="fill"></span></div>
    <div class="field short"><span class="fill"></span></div>
    <div class="field"><span>Phone:</span><span class="fill"></span></div>
    <div class="field"><span>Email:</span><span class="fill"></span></div>
    <p class="thanks">thanks for participating</p>
  </form>

</main>
</body>
</html>
```